GlamFrocks.com Banner AD

We are looking for some talented creators to create for us a banner ad for our online clothing store that specializes in dresses. We are looking for a fresh, clean, and sleek LUMA, T&K, and Plume appeal- clean, modern and sophisticated.

We would like for the final project to appear professionally done, we've had projects completed by several talent out there that did not capture our image, and let's just say it was too cluttered and appeared as if a high school editor had completed it.

I have attached a few files for you to reference, I have File 1, 2, 3, 8 and the T&K photos as examples of what we DO like.

I have attached File 5, which is the work of one the designers that was working on this project. Although it is very simple and gets the point across, it doesn't come across like a magazine editorial.

I have attached File 6, that is the main photo we wish to use for our banner.

I have attached File 7, which is what a creator had done for us via Quickdo.com, that is a good example of what we do NOT want.

That is about sums it up! I hope the examples are useful tools for you!

Hi Designers!

Thank you so much for your submissions! I enjoy viewing each and every one of them! Please view my update on what I am looking for, I have made some adjustments and have added a few more examples to reference, I have made my direction a bit more clearer. Because it seems some designers are not quite understanding my direction. I know you all have amazing talent and I am hoping to see something I am looking for and I love soon! If you have any other questions, please don't hesitate to ask! 

Target Market(s)

Our company targets women of all ages, we carry dresses that cater to every occasion, whether its an older woman looking for a dress to attend a wedding or a teenager looking for a prom dress. We want our front page banner to appear fresh, clean, with a feminine touch, we want to stray from tacky (gradients, etc..) and keep it classy all while maintaining that magazine editorial element, we want to be more fashion focused, like Plume. We want this project to appear professionally done. Our desired concept is something out of a magazine editorial, not too much going on, while shifting focus more on the dress itself than a design element like flowers or spring backgrounds.

Industry/Entity Type

High School

Requirements
Must have
• We want a plume fashion appeal, magazine editorial type of look. The phrases below should be included"

"New Season New Sexy Dresses"

"Free U.S shipping on orders $75+"
"Shop our sales up to 60% off"

All of the other phrases do not need to be included. Also, Do not include the parenthesis.
Should not have
• Only include the photo I've attached that appears solo. Please do not include the other 3 dresses that is displayed in a banner that was created for us by another designer. (that is provided as an example only)

```html
<!DOCTYPE html>
<html lang="en">
<head>
<meta charset="utf-8">
<title>New Season Dresses Banner</title>
<link href="https://fonts.googleapis.com/css2?family=Marcellus&family=Dancing+Script:wght@500&display=swap" rel="stylesheet">
<style>
  :root {
    --bg-light: #ffffff;
    --bg-shade: #e6e6e6;
    --ink: #1c1c1c;
    --ribbon: #0f1a16;
    --ribbon-fold: #050807;
    --pink: #ee4d86;
    --panel: #fbeff3;
    --rule: #b9b9b9;
    --white: #ffffff;
    --photo-warm: #d8b89a;
    --photo-dress: #2f3a4f;
    --photo-pink: #d9569a;
    --photo-green: #6fb98a;
  }
  * { margin: 0; padding: 0; box-sizing: border-box; }
  html, body { width: 1200px; height: 1043px; overflow: hidden; }
  body {
    background: radial-gradient(ellipse at 70% 40%, var(--bg-light) 0%, var(--bg-light) 40%, var(--bg-shade) 100%);
  }
  .banner {
    position: relative;
    width: 1200px;
    height: 1043px;
    overflow: hidden;
  }
  .model-photo {
    position: absolute;
    left: 60px;
    top: 0;
    width: 500px;
    height: 1043px;
    background: linear-gradient(180deg,
      var(--photo-warm) 0%,
      var(--photo-warm) 28%,
      var(--photo-dress) 44%,
      var(--photo-pink) 62%,
      var(--photo-green) 80%,
      var(--photo-dress) 100%);
    opacity: 0.85;
  }
  .copy {
    position: absolute;
    left: 656px;
    top: 0;
    width: 356px;
    height: 1043px;
    text-align: center;
    color: var(--ink);
  }
  .headline {
    position: absolute;
    left: 0;
    width: 100%;
    font-family: "Marcellus", serif;
    font-weight: 400;
    letter-spacing: 1px;
  }
  .headline--season { top: 70px; font-size: 84px; line-height: 74px; }
  .headline--dresses { top: 312px; font-size: 66px; line-height: 60px; }
  .rule {
    position: absolute;
    left: 16px;
    width: 324px;
    height: 2px;
    background: linear-gradient(90deg, transparent, var(--rule) 20%, var(--rule) 80%, transparent);
  }
  .rule--top { top: 264px; }
  .rule--mid { top: 764px; }
  .sale-ribbon { position: absolute; left: 17px; top: 486px; width: 322px; height: 109px; }
  .sale-label {
    position: absolute;
    left: 0; top: 490px; width: 356px;
    font-family: "Marcellus", serif;
    font-size: 68px;
    line-height: 86px;
    color: var(--pink);
    letter-spacing: 2px;
  }
  .promo {
    position: absolute;
    left: 0;
    width: 100%;
    font-family: "Dancing Script", cursive;
    font-weight: 500;
    color: var(--ink);
  }
  .promo--sale { top: 642px; font-size: 48px; line-height: 54px; }
  .promo--shipping { top: 784px; font-size: 40px; line-height: 48px; }
  .shop-button { position: absolute; left: 15px; top: 911px; width: 325px; height: 72px; }
  .shop-label {
    position: absolute;
    left: 66px; top: 911px; width: 262px;
    font-family: "Marcellus", serif;
    font-size: 34px;
    line-height: 64px;
    color: var(--white);
    letter-spacing: 1px;
    text-align: center;
  }
</style>
</head>
<body>
  <main class="banner">
    <div class="model-photo" role="img" aria-label="Photo of a woman with long wavy hair seen from behind, wearing a fitted low-back floral print dress"></div>

    <section class="copy">
      <h1 class="headline headline--season">NEW<br>SEASON</h1>
      <div class="rule rule--top"></div>
      <h2 class="headline headline--dresses">NEW SEXY<br>DRESSES</h2>

      <svg class="sale-ribbon" viewBox="0 0 322 109" aria-hidden="true">
        <polygon points="0,14 16,14 16,109 0,97" fill="var(--ribbon-fold)"/>
        <polygon points="322,14 306,14 306,109 322,97" fill="var(--ribbon-fold)"/>
        <rect x="10" y="0" width="302" height="98" fill="var(--ribbon)"/>
        <rect x="42" y="14" width="240" height="68" fill="var(--panel)"/>
      </svg>
      <p class="sale-label">SALE</p>

      <p class="promo promo--sale">Shop our sales<br>up to 60% off</p>
      <div class="rule rule--mid"></div>
      <p class="promo promo--shipping">Free U.S shipping<br>on orders $75+</p>

      <svg class="shop-button" viewBox="0 0 325 72" aria-hidden="true">
        <polygon points="0,10 14,10 14,72 0,64" fill="var(--ribbon-fold)"/>
        <polygon points="325,10 311,10 311,72 325,64" fill="var(--ribbon-fold)"/>
        <rect x="8" y="0" width="309" height="64" fill="var(--ribbon)"/>
        <circle cx="58" cy="32" r="12" fill="none" stroke="var(--pink)" stroke-width="3"/>
        <polygon points="54,25 54,39 65,32" fill="var(--pink)"/>
      </svg>
      <p class="shop-label">SHOP NOW</p>
    </section>
  </main>
</body>
</html>
```